Home Services Website Design and Revisions

We have started to create a website but I would like to get some ideas and a quote on how to create a more professional website then what we have created thus far.

http://brindlehomeworks.example/

Pages I would need on the site

Home page - company summary and brand promise
who we are
what we do - services offered
our promise to quality and client experience
client experiences - testimonials and pictures
Promotions
Career opportunities - Join The team
Updates

Target Market(s)

Homeowners in the DFW region

Industry/Entity Type

Home Improvement

Number of Pages Required

5+ page

Font styles to use
Sans Serif

Requirements
Must have
• Home page - company summary and brand promise
• who we are
• what we do - services offered
• our promise to quality and client experience
• client experiences - testimonials and pictures
• Promotions
• Career opportunities - Join The team
• logo
• pictures
• links to social media sites
• A very impactful home page
• With a image of home and family.
• a beautiful home, yard and pictures of a loving family smiling and enjoying their home.
Nice to have
• Pictures with people to create emotion
• we don't work on houses
• we work on homes with families that trust us to provide quality services in a timely manner
• Families that trust us as their partner when they need work at their home with their family
Should not have
• low quality images or images just of homes

```html
<!DOCTYPE html>
<html lang="en">
<head>
<meta charset="utf-8">
<title>Brindle Homeworks – Who We Are</title>
<link href="https://fonts.googleapis.com/css2?family=Open+Sans:wght@400;600&family=Raleway:wght@400;500&display=swap" rel="stylesheet">
<style>
:root{
  --green:#5fb90d;
  --text:#555;
  --dark:#222;
  --muted:#666;
  --footer:#f7f7f7;
  --white:#fff;
  --line:#dcdcdc;
}
*{box-sizing:border-box;margin:0;padding:0}
html,body{width:1200px;height:941px;overflow:hidden;background:var(--white)}
body{position:relative;font-family:"Open Sans",sans-serif;color:var(--text)}
.abs{position:absolute}
h1,h2,h3,h4{font-family:"Raleway",sans-serif;font-weight:400;color:var(--dark)}

/* header */
.site-header{left:0;top:0;width:1200px;height:47px;background:var(--white)}
.brand{left:89px;top:6px;display:flex;align-items:center;gap:8px}
.brand-mark{width:22px;height:22px;background:var(--green)}
.brand-name{font-family:"Open Sans",sans-serif;font-weight:600;font-size:15px;color:var(--dark);line-height:1}
.brand-tag{left:119px;top:31px;font-size:6px;color:var(--dark);letter-spacing:.2px}
.main-nav{right:89px;top:17px;display:flex;gap:21px;font-size:12px;color:var(--dark)}
.main-nav .active{color:var(--green);position:relative}
.main-nav .active::after{content:"";position:absolute;left:-2px;right:-2px;top:29px;height:2px;background:var(--green)}

/* title band */
.page-band{left:0;top:47px;width:1200px;height:68px;background:var(--green)}
.page-band h1{position:absolute;left:89px;top:20px;font-size:20px;color:var(--white)}
.breadcrumb{position:absolute;right:89px;top:27px;font-size:11.5px;font-weight:600;color:var(--white)}

/* intro */
.photo-frame{background:var(--white);padding:8px;box-shadow:0 2px 6px rgba(0,0,0,.15)}
.photo-back{left:92px;top:173px;width:200px;height:185px}
.photo-front{left:188px;top:228px;width:261px;height:189px}
.photo{width:100%;height:100%}
.photo-back .photo{background:linear-gradient(135deg,#bfe7ee,#e9f1f2 60%,#b98a5c)}
.photo-front .photo{background:linear-gradient(160deg,#f3f3f3,#dedbd8 60%,#c9b79a)}
.intro h2{left:512px;top:165px;font-size:25px}
.intro p{left:515px;top:204px;width:598px;font-size:11.6px;line-height:22px}
.btn{display:block;background:var(--green);color:var(--white);font-size:11.6px;text-align:center}
.read-more{left:515px;top:358px;width:113px;height:38px;line-height:38px}

/* about + features */
.about h2{left:92px;top:465px;font-size:21px}
.about p{left:92px;top:501px;width:372px;font-size:11.6px;line-height:22px}
.feature-icon{width:42px;height:42px;border-radius:50%;background:var(--green);display:flex;align-items:center;justify-content:center}
.feature h3{position:absolute;font-size:19px;top:0}
.feature p{position:absolute;top:30px;width:230px;font-size:11.6px;line-height:22px;color:var(--muted)}
.feature{width:300px;height:110px}
.feature .feature-icon{position:absolute;left:-61px;top:1px}
.feature h3{left:0}
.feature p{left:-3px}

/* footer */
.site-footer{left:0;top:720px;width:1200px;height:187px;background:var(--footer)}
.site-footer h4{position:absolute;top:15px;font-size:16px}
.footer-about p{position:absolute;left:89px;top:47px;width:230px;font-size:11.6px;line-height:19.5px;color:var(--muted)}
.social{position:absolute;left:89px;top:119px;display:flex;gap:6px}
.social span{width:32px;height:32px;border-radius:50%}
.links{position:absolute;left:397px;top:47px;list-style:none;font-size:11.6px;line-height:22.2px;color:var(--muted)}
.contact{position:absolute;left:597px;display:flex;align-items:center;gap:10px;font-size:11.6px;color:var(--dark)}
.contact-icon{width:29px;height:29px;background:var(--green);display:flex;align-items:center;justify-content:center}
.email-field{position:absolute;left:872px;top:44px;width:229px;height:36px;border:1px solid var(--line);background:var(--white);font-size:11.6px;color:var(--muted);padding:10px 11px}
.send{position:absolute;left:872px;top:88px;width:113px;height:35px;line-height:35px}
.bottom-bar{left:0;top:907px;width:1200px;height:34px;background:var(--green)}
.bottom-bar p{position:absolute;left:90px;top:8px;font-size:11.6px;color:var(--white)}
.to-top{left:1068px;top:881px;width:48px;height:48px;border-radius:50%;background:var(--white);border:1px solid var(--line);display:flex;align-items:center;justify-content:center}
</style>
</head>
<body>

<header class="site-header abs">
  <div class="brand abs"><span class="brand-mark"></span><span class="brand-name">Brindle Homeworks</span></div>
  <div class="brand-tag abs">• PAINTING • LANDSCAPING/MOWING • WINDOW WASHING • MAID SERVICES</div>
  <nav class="main-nav abs">
    <span class="active">Home</span><span>Who we are</span><span>What we do</span><span>Client experiences</span><span>Career Opportunities</span>
  </nav>
</header>

<section class="page-band abs">
  <h1>Who We Are</h1>
  <div class="breadcrumb">Home / Who We Are</div>
</section>

<section class="intro">
  <div class="photo-frame photo-back abs"><div class="photo" role="img" aria-label="Mother and young daughter by a bright window"></div></div>
  <div class="photo-frame photo-front abs"><div class="photo" role="img" aria-label="Smiling girl lying on a clean living room floor"></div></div>
  <h2 class="abs">Who We Are</h2>
  <p class="abs">Lorem Ipsum is simply dummy text of the printing and typesetting industry. Lorem Ipsum has been the industry's standard dummy text ever since the 1500s, when an unknown printer took a galley of type and scrambled it to make a type specimen book. It has survived not only five centuries, but also the leap into electronic typesetting, remaining essentially unchanged. It was popularised in the 1960s with the release of Letraset sheets containing Lorem Ipsum passages, and more recently with desktop publishing software like Aldus PageMaker including versions of Lorem Ipsum.</p>
  <a class="btn read-more abs">Read More</a>
</section>

<section class="about">
  <h2 class="abs">About the firm</h2>
  <p class="abs">Lorem Ipsum is simply dummy text of the printing and typesetting industry. Lorem Ipsum has been the industry's standard dummy text ever since the 1500s, when an unknown printer took a galley of type and scrambled it to make a type specimen book. It has survived not only five centuries, but also the leap into electronic typesetting, remaining essentially unchanged. It was popularised in the 1960s with the release of Letraset.</p>
</section>

<div class="feature abs" style="left:548px;top:466px">
  <div class="feature-icon"><svg width="20" height="20" viewBox="0 0 20 20" fill="none" stroke="#fff" stroke-width="1.5"><path d="M6 2h8v6a4 4 0 0 1-8 0z"/><path d="M6 4H3a3 3 0 0 0 3 4M14 4h3a3 3 0 0 1-3 4M10 12v4M6 18h8"/></svg></div>
  <h3>Success Story</h3>
  <p>Lorem Ipsum is simply dummy text of the printing and typesetting industry. Lorem Ipsum has been the industry's.</p>
</div>
<div class="feature abs" style="left:895px;top:466px">
  <div class="feature-icon"><svg width="24" height="16" viewBox="0 0 24 16" fill="#fff"><path d="M0 16 8 4l4 5 4-7 8 14z"/></svg></div>
  <h3>Our Mission</h3>
  <p>Lorem Ipsum is simply dummy text of the printing and typesetting industry. Lorem Ipsum has been the industry's.</p>
</div>
<div class="feature abs" style="left:548px;top:585px">
  <div class="feature-icon"><svg width="20" height="18" viewBox="0 0 20 18" fill="#fff"><circle cx="7" cy="4" r="3"/><path d="M1 18v-5a6 6 0 0 1 12 0v5z"/><rect x="14" y="10" width="2" height="8"/><rect x="17" y="6" width="2" height="12"/></svg></div>
  <h3>Our Vision</h3>
  <p>Lorem Ipsum is simply dummy text of the printing and typesetting industry. Lorem Ipsum has been the industry's.</p>
</div>
<div class="feature abs" style="left:895px;top:585px">
  <div class="feature-icon"><svg width="16" height="22" viewBox="0 0 16 22" fill="none" stroke="#fff" stroke-width="1.5"><rect x="3" y="1" width="10" height="8"/><path d="M8 9v3"/><path fill="#fff" stroke="none" d="m8 12 2 4 4 .5-3 3 .8 4-3.8-2-3.8 2 .8-4-3-3 4-.5z"/></svg></div>
  <h3>Our Values</h3>
  <p>Lorem Ipsum is simply dummy text of the printing and typesetting industry. Lorem Ipsum has been the industry's.</p>
</div>

<footer class="site-footer abs">
  <div class="footer-about">
    <h4 style="left:89px">About Us</h4>
    <p>Lorem Ipsum is simply dummy text of the printing and typesetting industry. Lorem Ipsum has been the industry's</p>
    <div class="social">
      <span style="background:#3b5998" role="img" aria-label="Social link"></span>
      <span style="background:#1dc6f5" role="img" aria-label="Social link"></span>
      <span style="background:#dd2d22" role="img" aria-label="Social link"></span>
      <span style="background:#145483" role="img" aria-label="Social link"></span>
    </div>
  </div>
  <h4 style="left:397px">Useful Links</h4>
  <ul class="links"><li>Site Map</li><li>Email</li><li>Privacy Policy</li><li>Terms of Service</li><li>Delivery and Returns</li></ul>
  <h4 style="left:597px">Get In Touch</h4>
  <div class="contact" style="top:48px"><span class="contact-icon"><svg width="12" height="12" viewBox="0 0 12 12" fill="#fff"><path d="M2 0h2l1 3-1.5 1a7 7 0 0 0 4.5 4.5L9 7l3 1v2a2 2 0 0 1-2 2A10 10 0 0 1 0 2a2 2 0 0 1 2-2z"/></svg></span>123 -456-7890</div>
  <div class="contact" style="top:89px"><span class="contact-icon"><svg width="13" height="9" viewBox="0 0 13 9" fill="none" stroke="#fff" stroke-width="1.2"><rect x=".6" y=".6" width="11.8" height="7.8"/><path d="m.6.6 5.9 4.5L12.4.6"/></svg></span>info@domain.com</div>
  <h4 style="left:871px">Newsletter</h4>
  <div class="email-field">Email</div>
  <a class="btn send">SEND</a>
</footer>

<div class="bottom-bar abs"><p>Copyright 2016 | All Right Reserved</p></div>
<div class="to-top abs"><svg width="10" height="6" viewBox="0 0 10 6" fill="none" stroke="#5fb90d" stroke-width="1.6"><path d="M1 5 5 1l4 4"/></svg></div>

</body>
</html>
```